HOME PAGE AND AND SECONDARY DESIGN FOR INTERNAL PAGES

Construction company looking for an easy to navagate professional serious greyscale website with a good clean feel simple clean menu and responsive friendly design. Our main clientele is commercial properties business owners and investors of rental properties. This website is going to be static HTML5 and would need multiple sizing files for clean fast rendering. Clean and accurate design files a must so if your experienced awesome modern greyscale designer let's get started I need this done as soon as possible.

Industry/Entity Type

construction, electrical, plumbing, commercial build outs

Number of Pages Required

2 page

Font styles to use
Sans Serif

Colors

Designer to choose only greyscale colors for use in the design.

Requirements
Must have
• Main Menu... Home, Services, Projects, About our team

```html
<!DOCTYPE html>
<html lang="en">
<head>
<meta charset="utf-8">
<title>Ironline Builders — Home</title>
<link rel="stylesheet" href="https://fonts.googleapis.com/css2?family=Krona+One&family=Kanit:wght@300;400;500&display=swap">
<style>
:root{
  --black:#0d0d0d;
  --ink:#222;
  --dark:#3a3a3a;
  --mid:#555;
  --grey:#6b6b6b;
  --soft:#9a9a9a;
  --line:#c9c9c9;
  --panel:#d9d9d9;
  --paper:#f2f2f2;
  --white:#fff;
  --head:"Krona One", sans-serif;
  --body:"Kanit", sans-serif;
}
*{margin:0;padding:0;box-sizing:border-box}
html,body{width:1200px;height:5145px;overflow:hidden}
body{position:relative;background:var(--paper);font-family:var(--body);font-weight:300;color:var(--ink)}
section,header,footer{position:absolute;left:0;width:1200px}
.abs{position:absolute}
h1,h2,h3{font-family:var(--head);font-weight:400;text-transform:uppercase;letter-spacing:1px}
p{font-size:12.5px;line-height:21px}
.btn{position:absolute;display:flex;align-items:center;justify-content:center;background:var(--mid);color:var(--white);font-family:var(--head);font-size:12px;letter-spacing:.5px;text-transform:uppercase}
.circle-btn{position:absolute;width:54px;height:54px;border-radius:50%;border:1.5px solid var(--soft);display:flex;align-items:center;justify-content:center}

/* top bar + header */
.topbar{top:0;height:18px;background:var(--ink);color:#bbb;font-size:9px;display:flex;align-items:center}
.topbar span{position:absolute}
.site-header{top:18px;height:74px;background:var(--white)}
.nav{position:absolute;top:0;height:74px;display:flex;align-items:center;gap:46px;font-size:12px;font-weight:400;color:var(--ink)}
.nav-cta{top:16px;left:986px;width:124px;height:40px;font-size:13px}
.brand{position:absolute;left:400px;top:0;width:400px;height:74px;display:flex;align-items:center;justify-content:center;font-family:var(--head);font-size:15px;color:var(--dark);letter-spacing:1px}

/* hero */
.hero{top:92px;height:598px;background:var(--black)}
.hero-photo{position:absolute;left:600px;top:0;width:600px;height:598px;background:linear-gradient(160deg,#d8d8d8 0%,#8a8a8a 40%,#2a2a2a 100%)}
.hero-photo-left{position:absolute;left:0;top:0;width:600px;height:598px;background:linear-gradient(120deg,#050505 0%,#2b2b2b 55%,#555 100%)}
.hero h1{position:absolute;left:148px;top:232px;font-size:52px;line-height:64px;color:var(--white)}
.hero p{position:absolute;left:868px;top:402px;width:220px;color:var(--white);font-size:12px}
.hero .scroll{left:1072px;top:516px;width:34px;height:34px;border-color:#ccc;color:#ccc}

/* about */
.about{top:690px;height:546px;background:var(--paper)}
.about-photo{position:absolute;left:0;top:0;width:675px;height:546px;background:linear-gradient(100deg,#e6e6e6 0%,#bdbdbd 45%,#8c8c8c 70%,#e8e8e8 100%)}
.about-panel{position:absolute;left:675px;top:0;width:525px;height:546px;background:var(--panel)}
.about h2{position:absolute;right:92px;top:200px;font-size:38px;color:var(--ink)}
.about p{position:absolute;right:92px;top:262px;width:330px;text-align:right;font-size:12px}
.about .btn{left:960px;top:400px;width:148px;height:40px}

/* services */
.services{top:1236px;height:644px;background:var(--white)}
.services h2{position:absolute;left:148px;top:88px;font-size:38px}
.services .prev{left:982px;top:80px}
.services .next{left:1054px;top:80px}
.service-card{position:absolute;top:182px;height:424px;overflow:hidden}
.service-card .fill{position:absolute;inset:0}
.service-card h3{position:absolute;left:80px;top:284px;font-size:22px;color:var(--white)}
.service-card p{position:absolute;left:80px;top:322px;width:470px;font-size:10.5px;line-height:19px;color:#ddd}

/* advantages */
.advantages{top:1880px;height:628px;background:var(--white)}
.advantages h2{position:absolute;left:0;width:1200px;text-align:center;top:70px;font-size:38px}
.adv{position:absolute;top:162px;width:230px;height:370px}
.adv .icon{width:90px;height:90px;border-radius:50%;border:1.5px solid var(--soft);display:flex;align-items:center;justify-content:center}
.adv h3{margin-top:28px;font-size:12px;letter-spacing:.5px}
.adv h3 b{font-size:18px;font-weight:400}
.adv p{margin-top:22px;width:180px;font-size:12px}
.adv-divider{position:absolute;top:162px;width:1px;height:360px;background:#e2e2e2}

/* testimonial */
.trust{top:2508px;height:546px;background:var(--grey)}
.trust-band{position:absolute;left:420px;top:0;width:378px;height:546px;background:var(--mid)}
.trust-photo{position:absolute;left:798px;top:0;width:402px;height:546px;background:linear-gradient(150deg,#f0f0f0 0%,#bcbcbc 45%,#4a4a4a 100%)}
.trust h2{position:absolute;left:148px;top:130px;font-size:38px;line-height:49px;color:var(--white)}
.trust .prev{left:460px;top:272px;color:var(--white);border-color:#ddd}
.trust .next{left:530px;top:272px;color:var(--white);border-color:#ddd}
.trust blockquote{position:absolute;left:462px;top:360px;width:292px;font-size:12px;line-height:19px;color:var(--white)}
.trust .name{position:absolute;left:462px;top:478px;font-family:var(--head);font-size:12px;color:var(--white)}
.trust .role{position:absolute;left:462px;top:498px;font-size:9px;color:#ddd}

/* projects */
.projects{top:3054px;height:1031px;background:var(--paper)}
.projects h2{position:absolute;left:0;width:1200px;text-align:center;top:90px;font-size:38px;line-height:49px}
.project{position:absolute;overflow:hidden}
.project h3{position:absolute;left:36px;font-size:16px;color:var(--white)}
.project .addr{position:absolute;left:36px;font-size:11px;color:#ddd;display:flex;gap:8px;align-items:center}
.projects .btn{left:490px;top:896px;width:220px;height:40px}

/* contact */
.contact{top:4085px;height:800px;background:var(--grey)}
.contact h2{position:absolute;left:148px;top:140px;font-size:38px;line-height:49px;color:var(--white)}
.contact .intro{position:absolute;left:734px;top:174px;width:290px;font-size:12px;line-height:19px;color:var(--white)}
.field{position:absolute;height:34px;border-bottom:1px solid #9c9c9c;color:#cfcfcf;font-size:11px}
.consent{position:absolute;left:148px;top:596px;display:flex;align-items:center;gap:10px;font-size:9px;color:var(--white)}
.consent i{width:10px;height:10px;background:var(--white);display:block}
.consent u{text-decoration:underline}
.contact .btn{left:932px;top:578px;width:120px;height:40px;background:var(--mid)}

.footer-card{position:absolute;left:148px;top:4765px;width:904px;height:276px;background:#1b1b1b;z-index:2}
.footer-map{position:absolute;left:452px;top:0;width:452px;height:276px;background:linear-gradient(135deg,#3d3d3d,#2a2a2a)}
.footer-info{position:absolute;left:84px;top:74px;color:#e6e6e6;font-size:11.5px;line-height:16px}
.footer-info .row{display:flex;gap:12px;align-items:flex-start;margin-bottom:20px}
.socials{display:flex;gap:12px;margin-left:6px}
.socials i{width:10px;height:10px;border-radius:50%;background:#ddd;display:block}
.footer-brand{position:absolute;left:302px;top:126px;width:300px;text-align:center;font-family:var(--head);font-size:13px;color:var(--white);letter-spacing:1px}
.copyright{position:absolute;left:148px;top:5086px;font-size:11px;color:var(--dark)}
.policy{position:absolute;left:968px;top:5080px;font-size:11px;color:var(--dark)}
</style>
</head>
<body>

<div class="topbar" style="position:absolute;left:0;width:1200px">
  <span style="left:148px">⌖ 4120 Ridgeview Drive Ste 200, Austin, Texas 78745</span>
  <span style="left:870px">✉ info@ironlinebuilders.com</span>
  <span style="left:1040px">☏ 512-555-0148</span>
</div>

<header class="site-header">
  <nav class="nav" style="left:148px"><span>HOME</span><span>SERVICES</span><span>PROJECTS</span></nav>
  <div class="brand">IRONLINE BUILDERS</div>
  <nav class="nav" style="left:828px"><span>ABOUT OUR TEAM</span></nav>
  <span class="btn nav-cta">CONTACT</span>
</header>

<section class="hero">
  <div class="hero-photo-left" role="img" aria-label="Low-angle greyscale view of a glass office tower"></div>
  <div class="hero-photo" role="img" aria-label="Greyscale skyscraper facade against a bright cloudy sky"></div>
  <svg class="abs" style="left:600px;top:300px" width="600" height="298"><polygon points="0,298 300,30 600,200 600,298" fill="#0d0d0d"/></svg>
  <h1>We build<br>commercial<br>real estate</h1>
  <p>Lorem ipsum dolor sit amet consectetur. Amet sed magna pulvinar a sagittis vitae turpis est. Curabitur risus condimentum eget elementum vulputate lectus nulla.</p>
  <span class="circle-btn scroll"><svg width="12" height="14"><path d="M6 1v11M2 8l4 4 4-4" stroke="#ccc" fill="none"/></svg></span>
</section>

<section class="about">
  <div class="about-photo" role="img" aria-label="Two engineers in hard hats reviewing building plans"></div>
  <div class="about-panel"></div>
  <h2>About us</h2>
  <p>Nibh mattis faucibus gravida eget platea cras ultrices sed mattis. Scelerisque viverra in a arcu ornare ac at habitant nunc. Id a mauris in sed. Adipiscing sed quis ipsum aliquam fames morbi porttitor sit interdum. Sed lacus tortor.</p>
  <span class="btn">Read more</span>
</section>

<section class="services">
  <h2>Our services</h2>
  <span class="circle-btn prev"><svg width="20" height="10"><path d="M19 5H2M6 1L2 5l4 4" stroke="#777" fill="none"/></svg></span>
  <span class="circle-btn next"><svg width="20" height="10"><path d="M1 5h17M14 1l4 4-4 4" stroke="#777" fill="none"/></svg></span>
  <div class="service-card" style="left:148px;width:638px">
    <div class="fill" role="img" aria-label="Tower crane over a city skyline at dusk" style="background:linear-gradient(180deg,#6f6f6f 0%,#9a9a9a 35%,#3a3a3a 70%,#111 100%)"></div>
    <h3>Construction</h3>
    <p>Nibh mattis faucibus gravida eget platea cras ultrices sed mattis. Scelerisque viverra in a arcu ornare ac at habitant nunc. Id a mauris in sed. Adipiscing sed quis ipsum aliquam fames morbi porttitor sit interdum. Sed lacus tortor.</p>
  </div>
  <div class="service-card" style="left:836px;width:364px">
    <div class="fill" role="img" aria-label="Consultants reviewing documents in an office" style="background:linear-gradient(180deg,#bcbcbc 0%,#7a7a7a 40%,#222 100%)"></div>
    <h3 style="left:80px">Consulting</h3>
    <p>Nibh mattis faucibus gravida eget platea cras ultrices sed mattis. Scelerisque viverra in a arcu ornare ac at habitant nunc. Id a mauris in sed. Adipiscing sed quis ipsum aliquam fames morbi porttitor sit interdum. Sed lacus tortor.</p>
  </div>
</section>

<section class="advantages">
  <h2>Our advantages</h2>
  <div class="adv-divider" style="left:352px"></div>
  <div class="adv-divider" style="left:602px"></div>
  <div class="adv-divider" style="left:852px"></div>
  <div class="adv" style="left:148px">
    <div class="icon"><svg width="44" height="44" fill="none" stroke="#555" stroke-width="2"><circle cx="22" cy="22" r="17"/><circle cx="22" cy="22" r="8"/><path d="M22 2v8M22 34v8M2 22h8M34 22h8"/></svg></div>
    <h3><b>#1</b> Customer focus</h3>
    <p>Nibh mattis faucibus gravida eget platea cras ultrices sed mattis. Scelerisque viverra in a arcu ornare ac at habitant nunc. Id a mauris in sed. Adipiscing sed quis ipsum aliquam fames morbi porttitor sit interdum. Sed lacus tortor.</p>
  </div>
  <div class="adv" style="left:382px">
    <div class="icon"><svg width="44" height="44" fill="#555"><circle cx="22" cy="10" r="5"/><circle cx="10" cy="28" r="4"/><circle cx="34" cy="28" r="4"/><circle cx="22" cy="28" r="4"/><rect x="4" y="35" width="36" height="4" rx="2"/></svg></div>
    <h3><b>#2</b> Multi experience</h3>
    <p>Nibh mattis faucibus gravida eget platea cras ultrices sed mattis. Scelerisque viverra in a arcu ornare ac at habitant nunc. Id a mauris in sed. Adipiscing sed quis ipsum aliquam fames morbi porttitor sit interdum. Sed lacus tortor.</p>
  </div>
  <div class="adv" style="left:632px">
    <div class="icon"><svg width="44" height="44" fill="#555"><rect x="12" y="4" width="20" height="10" rx="2"/><circle cx="10" cy="22" r="5"/><circle cx="34" cy="22" r="5"/><rect x="3" y="29" width="14" height="12" rx="3"/><rect x="27" y="29" width="14" height="12" rx="3"/><rect x="16" y="30" width="12" height="3"/></svg></div>
    <h3><b>#3</b> Professionalism</h3>
    <p>Nibh mattis faucibus gravida eget platea cras ultrices sed mattis. Scelerisque viverra in a arcu ornare ac at habitant nunc. Id a mauris in sed. Adipiscing sed quis ipsum aliquam fames morbi porttitor sit interdum. Sed lacus tortor.</p>
  </div>
  <div class="adv" style="left:880px">
    <div class="icon"><svg width="44" height="44" fill="#555"><circle cx="24" cy="9" r="5"/><rect x="18" y="16" width="12" height="12" rx="3"/><path d="M4 32h10l8 4h14a3 3 0 0 1 0 6H4z"/></svg></div>
    <h3><b>#4</b> 24/7 support</h3>
    <p>Nibh mattis faucibus gravida eget platea cras ultrices sed mattis. Scelerisque viverra in a arcu ornare ac at habitant nunc. Id a mauris in sed. Adipiscing sed quis ipsum aliquam fames morbi porttitor sit interdum. Sed lacus tortor.</p>
  </div>
</section>

<section class="trust">
  <div class="trust-band"></div>
  <div class="trust-photo" role="img" aria-label="Portrait of a smiling business client in a suit"></div>
  <h2>Our<br>customers<br>trust us</h2>
  <span class="circle-btn prev"><svg width="20" height="10"><path d="M19 5H2M6 1L2 5l4 4" stroke="#fff" fill="none"/></svg></span>
  <span class="circle-btn next"><svg width="20" height="10"><path d="M1 5h17M14 1l4 4-4 4" stroke="#fff" fill="none"/></svg></span>
  <blockquote>"Nibh mattis faucibus gravida eget platea cras ultrices sed mattis. Scelerisque viverra in a arcu ornare ac at habitant nunc. Id a mauris in sed. Adipiscing sed quis ipsum aliquam fames morbi porttitor sit interdum. Sed lacus tortor."</blockquote>
  <div class="name">DANA WHITFIELD</div>
  <div class="role">Lorem ipsum</div>
</section>

<section class="projects">
  <h2>We realize your<br>building project</h2>
  <div class="project" style="left:148px;top:246px;width:452px;height:290px;background:linear-gradient(180deg,#9a9a9a,#3c3c3c 70%,#1e1e1e)" role="img" aria-label="Glass office buildings in fog">
    <h3 style="top:222px">Lorem ipsum</h3>
    <div class="addr" style="top:248px"><svg width="8" height="11"><path d="M4 11C1 7 0 5 0 4a4 4 0 0 1 8 0c0 1-1 3-4 7z" fill="#ddd"/></svg>2207 Maple Ct. Riverton, Ohio 44012</div>
  </div>
  <div class="project" style="left:600px;top:214px;width:452px;height:322px;background:linear-gradient(170deg,#cfcfcf,#7a7a7a 50%,#2b2b2b)" role="img" aria-label="Residential tower under construction with cranes">
    <h3 style="top:258px">Lorem ipsum</h3>
    <div class="addr" style="top:284px"><svg width="8" height="11"><path d="M4 11C1 7 0 5 0 4a4 4 0 0 1 8 0c0 1-1 3-4 7z" fill="#ddd"/></svg>2207 Maple Ct. Riverton, Ohio 44012</div>
  </div>
  <div class="project" style="left:148px;top:536px;width:452px;height:324px;background:linear-gradient(180deg,#8a8a8a,#4a4a4a 50%,#151515)" role="img" aria-label="Workers on a concrete building site">
    <h3 style="top:256px">Lorem ipsum</h3>
    <div class="addr" style="top:282px"><svg width="8" height="11"><path d="M4 11C1 7 0 5 0 4a4 4 0 0 1 8 0c0 1-1 3-4 7z" fill="#ddd"/></svg>2207 Maple Ct. Riverton, Ohio 44012</div>
  </div>
  <div class="project" style="left:600px;top:536px;width:452px;height:290px;background:linear-gradient(160deg,#b0b0b0,#555 50%,#111)" role="img" aria-label="Modern building facade with angled slats">
    <h3 style="top:226px">Lorem ipsum</h3>
    <div class="addr" style="top:252px"><svg width="8" height="11"><path d="M4 11C1 7 0 5 0 4a4 4 0 0 1 8 0c0 1-1 3-4 7z" fill="#ddd"/></svg>2207 Maple Ct. Riverton, Ohio 44012</div>
  </div>
  <span class="btn">View all projects</span>
</section>

<section class="contact">
  <h2>Contact us for<br>a quality<br>consultation</h2>
  <p class="intro">"Nibh mattis faucibus gravida eget platea cras ultrices sed mattis. Scelerisque viverra in a arcu ornare ac at habitant nunc. Id a mauris in sed. Adipiscing sed quis ipsum aliquam fames morbi porttitor sit interdum. Sed lacus tortor."</p>
  <div class="field" style="left:148px;top:356px;width:426px">Full name *</div>
  <div class="field" style="left:626px;top:356px;width:426px">Company name *</div>
  <div class="field" style="left:148px;top:420px;width:426px">Email address *</div>
  <div class="field" style="left:626px;top:420px;width:426px">Phone number *</div>
  <div class="field" style="left:148px;top:514px;width:904px;height:36px">Your message</div>
  <div class="consent"><i></i>By clicking SEND US, you agree to our <u>Terms</u> and <u>Privacy Policy</u></div>
  <span class="btn">Send us</span>
</section>

<footer>
  <div class="footer-card">
    <div class="footer-map" role="img" aria-label="Street map showing the office location"></div>
    <div class="footer-info">
      <div class="row"><svg width="12" height="16"><path d="M6 15C2 10 1 8 1 6a5 5 0 0 1 10 0c0 2-1 4-5 9z" fill="none" stroke="#ddd" stroke-width="1.5"/></svg><span>4120 RIDGEVIEW DRIVE STE 200<br>AUSTIN, TEXAS 78745</span></div>
      <div class="row"><svg width="12" height="16"><rect x="2" y="1" width="8" height="14" rx="2" fill="none" stroke="#ddd" stroke-width="1.5"/></svg><span>512-555-0148</span></div>
      <div class="row"><svg width="12" height="16"><path d="M1 14L11 4M7 2l4 2-2 4" fill="none" stroke="#ddd" stroke-width="1.5"/></svg><span>info@ironlinebuilders.com</span></div>
      <div class="socials" aria-label="Social links"><i></i><i></i><i></i></div>
    </div>
    <div class="footer-brand">IRONLINE BUILDERS</div>
  </div>
  <div class="copyright">©Copyright 2023. IRONLINE BUILDERS LLC | All Rights Reserved</div>
  <div class="policy">Privacy Policy</div>
</footer>

</body>
</html>
```